A start up special flyer design!

Hi All - Have updated the attachment content - This is the info required for the designs.
I need a catchy flyer to send out to a few areas to advertise the start of my plumbing business!
The flyer will contain an offer for customers, which will need to have some key details on it. See attached. Feel free to fit these criteria into the flyer given your knowledge on design and messaging principles. Key thing to get across to customers is the discount and special offer, and that it is a start up offer.
I have a logo that needs to be on the flyer as well - let me know what format you require and I will send through to you.
The color scheme needs to be blue / grey / black / white.
Let me know if you have any questions.
I

```html
<!DOCTYPE html>
<html lang="en">
<head>
<meta charset="utf-8">
<title>Danny Flow Plumbing – Start-up Special Flyer</title>
<link href="https://fonts.googleapis.com/css2?family=Signika:wght@400;500;600&family=Arimo:wght@400&display=swap" rel="stylesheet">
<style>
  :root {
    --blue: #1a6dbd;
    --blue-deep: #0f4f93;
    --blue-light: #2f86d2;
    --grey: #7b7f84;
    --grey-dark: #5d6166;
    --paper: #eef0f2;
    --paper-light: #fbfbfc;
    --ink: #2a2c30;
    --white: #ffffff;
  }
  * { margin: 0; padding: 0; box-sizing: border-box; }
  html, body { width: 1200px; height: 806px; overflow: hidden; background: var(--paper); }
  .flyer {
    position: relative; width: 1200px; height: 806px; overflow: hidden;
    background: radial-gradient(ellipse at 70% 20%, var(--paper-light) 0%, var(--paper) 55%, #dfe2e5 100%);
    font-family: "Arimo", Arial, sans-serif; color: var(--ink);
  }
  .hero-curve { position: absolute; left: 0; top: 0; width: 1200px; height: 806px; }

  .brand {
    position: absolute; left: 560px; top: 120px; width: 470px; text-align: center;
    font-family: "Signika", sans-serif; font-weight: 600; font-size: 38px;
    letter-spacing: 1px; color: var(--blue);
  }
  .brand-dot {
    display: block; width: 26px; height: 26px; border-radius: 50%;
    background: var(--blue); margin: 0 auto 14px;
  }

  .services {
    position: absolute; left: 501px; top: 219px; width: 655px; height: 166px;
    background: linear-gradient(90deg, var(--blue-light) 0%, var(--blue) 60%, var(--blue-deep) 100%);
    padding: 16px 0 0 58px;
  }
  .services-fold {
    position: absolute; left: 1114px; top: 385px; width: 42px; height: 22px;
  }
  .services li {
    list-style: none; position: relative; font-family: "Signika", sans-serif;
    font-weight: 500; font-size: 25px; color: var(--white); height: 47px; line-height: 34px;
  }
  .services li svg { position: absolute; left: -42px; top: 4px; }

  .offer {
    position: absolute; left: 501px; top: 389px; width: 613px; height: 142px;
    background: linear-gradient(90deg, #8a8e93 0%, var(--grey) 50%, var(--grey-dark) 100%);
    padding: 6px 6px;
  }
  .offer-inner {
    border: 1.5px dashed rgba(255,255,255,0.8); height: 100%; padding: 8px 0 0 86px;
  }
  .offer li {
    list-style: none; position: relative; font-size: 17px; color: var(--white);
    height: 34px; line-height: 24px;
  }
  .offer li svg { position: absolute; left: -38px; top: 2px; }

  .terms {
    position: absolute; left: 598px; top: 542px; font-size: 15.5px; line-height: 26px; color: var(--ink);
  }
  .tools-photo {
    position: absolute; left: 390px; top: 540px; width: 196px; height: 160px; border-radius: 40% 30% 40% 30%;
    background: radial-gradient(ellipse at 55% 55%, #c9483d 0%, #a8adb3 45%, rgba(225,228,231,0) 72%);
  }
  .booking {
    position: absolute; left: 520px; top: 640px; width: 680px; height: 74px;
    background: rgba(255,255,255,0.75); padding: 8px 0 0 78px;
    font-family: "Signika", sans-serif; font-weight: 500; font-size: 21.5px;
    line-height: 27px; letter-spacing: 0.6px; color: var(--blue);
  }
  .contact-rule { position: absolute; left: 0; top: 715px; width: 1200px; height: 3px; background: var(--blue); }
  .contact-bar {
    position: absolute; left: 0; top: 724px; width: 1200px; height: 82px;
    background: linear-gradient(180deg, var(--blue-light) 0%, var(--blue) 100%);
    display: flex; align-items: center; padding-left: 233px; gap: 30px;
    font-size: 20px; color: var(--white);
  }
  .contact-item { display: flex; align-items: center; gap: 11px; }
  .contact-item svg { flex: none; }
  .contact-item.web { margin-left: 10px; }
</style>
</head>
<body>
<div class="flyer">
  <svg class="hero-curve" viewBox="0 0 1200 806" aria-hidden="false">
    <defs>
      <linearGradient id="heroTones" x1="0" y1="0" x2="1" y2="1">
        <stop offset="0" stop-color="#e7ecf4"/>
        <stop offset="0.35" stop-color="#f2a91f"/>
        <stop offset="0.6" stop-color="#7d8b5c"/>
        <stop offset="1" stop-color="#26324f"/>
      </linearGradient>
    </defs>
    <ellipse cx="140" cy="360" rx="430" ry="470" fill="var(--blue)"/>
    <ellipse cx="140" cy="360" rx="412" ry="452" fill="var(--white)"/>
    <ellipse cx="140" cy="360" rx="404" ry="444" fill="var(--blue)"/>
    <ellipse cx="140" cy="360" rx="396" ry="436" fill="var(--white)"/>
    <ellipse cx="140" cy="360" rx="388" ry="428" fill="var(--grey)"/>
    <ellipse cx="140" cy="360" rx="376" ry="416" fill="var(--white)"/>
    <ellipse cx="140" cy="360" rx="368" ry="408" fill="url(#heroTones)" role="img"
      aria-label="Photo of a tradesman's torso holding a yellow hard hat and hammer, wearing a tool belt full of tools, in front of a house"/>
  </svg>

  <div class="brand"><span class="brand-dot"></span>DANNY FLOW PLUMBING</div>

  <ul class="services">
    <li><svg width="26" height="28" viewBox="0 0 26 28"><path d="M2 6h12v3h4v5h-4V11H2z M6 3h6v3H6z" fill="#fff"/><path d="M16 17c0 3 -2 4 -2 6a2 2 0 0 0 4 0c0-2-2-3-2-6z" fill="#fff"/></svg>All plumbing, draining, and gasfitting works</li>
    <li><svg width="26" height="28" viewBox="0 0 26 28"><path d="M2 6h12v3h4v5h-4V11H2z M6 3h6v3H6z" fill="#fff"/><path d="M16 17c0 3 -2 4 -2 6a2 2 0 0 0 4 0c0-2-2-3-2-6z" fill="#fff"/></svg>“Quality work at a decent price”</li>
    <li><svg width="26" height="28" viewBox="0 0 26 28"><path d="M2 6h12v3h4v5h-4V11H2z M6 3h6v3H6z" fill="#fff"/><path d="M16 17c0 3 -2 4 -2 6a2 2 0 0 0 4 0c0-2-2-3-2-6z" fill="#fff"/></svg>“Local plumber”</li>
  </ul>
  <svg class="services-fold" viewBox="0 0 42 22" aria-hidden="true"><path d="M0 0h42v22z" fill="#16284f"/></svg>

  <div class="offer">
    <ul class="offer-inner">
      <li><svg width="14" height="20" viewBox="0 0 14 20"><path d="M7 1c1 5 6 7 6 12a6 6 0 0 1-12 0c0-3 2-4 3-7 1 2 1 3 2 4 1-3 1-6 1-9z" fill="none" stroke="#fff" stroke-width="1.6"/></svg>15% off your overall bill*</li>
      <li><svg width="14" height="20" viewBox="0 0 14 20"><path d="M7 1c1 5 6 7 6 12a6 6 0 0 1-12 0c0-3 2-4 3-7 1 2 1 3 2 4 1-3 1-6 1-9z" fill="none" stroke="#fff" stroke-width="1.6"/></svg>No GST payable, saving you additional 10% on your bill^</li>
      <li><svg width="14" height="20" viewBox="0 0 14 20"><path d="M7 1c1 5 6 7 6 12a6 6 0 0 1-12 0c0-3 2-4 3-7 1 2 1 3 2 4 1-3 1-6 1-9z" fill="none" stroke="#fff" stroke-width="1.6"/></svg>Plus, a free hot water health check and replacement quote~</li>
    </ul>
  </div>

  <div class="tools-photo" role="img" aria-label="Photo of plumbing tools: red pipe wrench, adjustable spanners, a brass tap and thread tape"></div>

  <div class="terms">
    *Offer valid between 15 August 2016 to 15 October 2016<br>
    ^Valid until 30 September 2016.<br>
    ~Quote valid for 12 months from the quote date.
  </div>

  <div class="booking">
    To make an appointment, call or email Danny, or<br>
    alternatively make a booking directly on the website
  </div>

  <div class="contact-rule"></div>
  <div class="contact-bar">
    <span class="contact-item">
      <svg width="22" height="22" viewBox="0 0 22 22"><rect width="22" height="22" rx="4" fill="#fff"/><path d="M7 4l3 3-2 2c1 2 3 4 5 5l2-2 3 3-2 3C10 18 4 12 4 6z" fill="var(--blue)"/></svg>
      0400 555 019
    </span>
    <span class="contact-item">
      <svg width="22" height="22" viewBox="0 0 22 22"><rect width="22" height="22" rx="4" fill="#fff"/><rect x="4" y="6" width="14" height="10" fill="none" stroke="var(--blue)" stroke-width="1.6"/><path d="M4 6l7 6 7-6" fill="none" stroke="var(--blue)" stroke-width="1.6"/></svg>
      danny@dannyflowplumbing.com
    </span>
    <span class="contact-item web">
      <svg width="22" height="22" viewBox="0 0 22 22"><circle cx="11" cy="11" r="11" fill="#fff"/><circle cx="11" cy="11" r="6.5" fill="none" stroke="var(--blue)" stroke-width="1.4"/><path d="M4.5 11h13M11 4.5c-3 3.5-3 9.5 0 13M11 4.5c3 3.5 3 9.5 0 13" fill="none" stroke="var(--blue)" stroke-width="1.2"/></svg>
      www.dannyflowplumbing.com
    </span>
  </div>
</div>
</body>
</html>
```